Wholesale company needs a sales brochure for our latest gadget- Nimbo Pebble. We sell to retailers

We need a sale brochure for our new product- Nimbo/Dart Pebble. It's an elegant little device that connects to any smartphone using an APP and let you locate your keys or your phone when you can't find them. We would like to see a design that uses the colors: Light blue, Black and metallic silver. The final design should communicate tech and innovative product. We need a total of 4 pages of 8.5x11'' (US letter size) to describe:
- Product benefits
- Product in use
- Display solution
- Profit generator
- Success story

Attached below are photos of the packaging and the display for your reference. Better photos will be sent later.
Please keep in mind that this product should be displayed on the counter with high foot traffic OR hang on hooks on a display fixture in the store.

This brochure will be used mainly to be sent digitally via email BUT we will also print it and will be mailing copies to our buyers.

Target Market(s)

Retailers and Distributors.
Small to mid-size retail stores:
- Electronic stores
- Convenient store
- Cellphone stores
- Gift stores

Industry/Entity Type

Retail

Font styles to use
Sans Serif

Colors
0692cd
ffffff
f3f1f8
33a6d7
85cae6

Requirements
Must have
• Must have:
• - "techie" and innovative look to go hand in hand with the product itself.
• - "in use" photos
• - "Description of the product"
• - Spec info
Nice to have
• Pattern or abstract design on background behind the text and images

```html
<!DOCTYPE html>
<html lang="en">
<head>
<meta charset="utf-8">
<title>Nimbo Pebble – Brochure Covers</title>
<link rel="stylesheet" href="https://fonts.googleapis.com/css2?family=Oswald:wght@400;500;600&family=Open+Sans:wght@600;700&display=swap">
<style>
  :root {
    --stage: #778a8c;
    --stage-line: #3c4647;
    --brand-blue: #1fa9e1;
    --ink: #000000;
    --paper: #ffffff;
    --silver: #d7dadd;
    --silver-dark: #9aa2a8;
    --label: #1a1a1a;
  }
  * { margin: 0; padding: 0; box-sizing: border-box; }
  html, body { width: 1200px; height: 848px; overflow: hidden; background: var(--stage); }
  .board { position: relative; width: 1200px; height: 848px; background: var(--stage); }
  .board-frame { position: absolute; left: 21px; top: 18px; width: 1158px; height: 812px; border: 1px solid var(--stage-line); }
  .page { position: absolute; top: 110px; width: 484px; height: 628px; background: var(--ink); box-shadow: 6px 8px 10px rgba(0,0,0,.45); overflow: hidden; }
  .page--front { left: 84px; }
  .page--back { left: 632px; }
  .page svg.shapes { position: absolute; inset: 0; }
  .glow { position: absolute; border-radius: 50%; background: radial-gradient(closest-side, rgba(190,195,200,.55), rgba(120,125,130,.2) 60%, rgba(0,0,0,0)); }
  .wordmark { position: absolute; font-family: "Oswald", sans-serif; font-weight: 600; color: var(--ink); white-space: nowrap; letter-spacing: -0.5px; }
  .wordmark sup { font-weight: 400; font-size: .3em; vertical-align: top; margin-left: 3px; }
  .page--front .wordmark { left: 56px; top: 70px; font-size: 64px; line-height: 1; }
  .photo { position: absolute; }
  .photo--package { left: 76px; top: 255px; width: 158px; height: 317px; background: linear-gradient(160deg, #f1f2f4, var(--silver) 55%, var(--silver-dark)); border-radius: 3px; }
  .headline { position: absolute; left: 288px; top: 250px; font-family: "Oswald", sans-serif; font-weight: 600; color: var(--paper); font-size: 47px; line-height: 66px; letter-spacing: .5px; }
  .intro { position: absolute; left: 288px; top: 520px; width: 138px; font-family: "Oswald", sans-serif; font-weight: 500; color: var(--paper); font-size: 9.4px; line-height: 12.6px; }
  .photo--display { left: 200px; top: 154px; width: 208px; height: 336px; background: linear-gradient(180deg, #1a1a1a 0 12%, #e9ecef 12% 28%, #2d5f86 28% 32%, #f2f3f5 32%); }
  .feature { position: absolute; display: flex; align-items: center; justify-content: flex-end; gap: 5px; padding: 0 4px 0 6px; background: linear-gradient(180deg, #ffffff, #cfd3d6); border-radius: 9px; font-family: "Open Sans", sans-serif; font-weight: 700; font-size: 8px; line-height: 9px; color: #333; text-align: right; }
  .feature span:first-child { white-space: nowrap; }
  .feature-icon { width: 28px; height: 26px; border-radius: 6px; background: var(--brand-blue); flex: none; }
  .feature--app { left: 84px; top: 262px; width: 84px; height: 34px; }
  .feature--phone { left: 49px; top: 337px; width: 127px; height: 34px; }
  .feature--setup { left: 101px; top: 414px; width: 74px; height: 30px; }
  .feature--setup .feature-icon { width: 22px; height: 22px; }
  .page--back .wordmark { left: 0; right: 0; text-align: center; top: 508px; font-size: 42px; line-height: 1; }
  .contact { position: absolute; left: 0; right: 0; top: 570px; text-align: center; font-family: "Oswald", sans-serif; color: #0b2633; }
  .contact-title { font-weight: 500; font-size: 13px; line-height: 16px; }
  .contact-line { font-weight: 400; font-size: 7.6px; line-height: 11px; }
  .caption { position: absolute; top: 780px; font-family: "Open Sans", sans-serif; font-weight: 600; font-size: 15px; color: var(--label); }
  .caption--front { left: 280px; }
  .caption--back { left: 838px; top: 777px; }
</style>
</head>
<body>
<main class="board">
  <div class="board-frame"></div>

  <section class="page page--front">
    <svg class="shapes" width="484" height="628" viewBox="0 0 484 628" aria-hidden="true">
      <polygon points="0,0 484,0 484,190 0,205" fill="var(--brand-blue)"/>
      <polygon points="157,0 484,0 484,44" fill="var(--ink)"/>
      <line x1="157" y1="0" x2="484" y2="44" stroke="#2b7fa8" stroke-width="1"/>
      <polygon points="0,621 484,610 484,628 0,628" fill="var(--brand-blue)"/>
      <line x1="0" y1="205" x2="484" y2="190" stroke="#0e4d6b" stroke-width="2"/>
    </svg>
    <div class="wordmark">Nimbo Pebble<sup>TM</sup></div>
    <div class="glow" style="left:20px;top:215px;width:270px;height:400px"></div>
    <div class="photo photo--package" role="img" aria-label="Retail blister pack of the Nimbo Pebble tracker, a blue triangular tag on a set of keys"></div>
    <h1 class="headline">FIND<br>YOUR<br>EVERY<br>THING</h1>
    <p class="intro">It's An Elegant Little Device That Connects To Any Smartphone Using An App And Let You Locate Your Keys Or Your Phone When You Can't Find Them.</p>
  </section>

  <section class="page page--back">
    <svg class="shapes" width="484" height="628" viewBox="0 0 484 628" aria-hidden="true">
      <polygon points="0,0 200,0 0,42" fill="var(--brand-blue)"/>
      <line x1="0" y1="42" x2="200" y2="0" stroke="#2b7fa8" stroke-width="1"/>
      <polygon points="0,474 484,495 484,610 0,620" fill="var(--brand-blue)"/>
      <line x1="0" y1="474" x2="484" y2="495" stroke="#0e4d6b" stroke-width="2"/>
    </svg>
    <div class="glow" style="left:130px;top:60px;width:340px;height:470px"></div>
    <div class="photo photo--display" role="img" aria-label="Counter display box filled with Nimbo Pebble packs in red, white, blue and black"></div>
    <div class="feature feature--app"><span>FREE APP<br>Tagly</span><span class="feature-icon"></span></div>
    <div class="feature feature--phone"><span>ANY PHONE<br>COMPATIBLE</span><span class="feature-icon"></span></div>
    <div class="feature feature--setup"><span>SET UP IN<br>1 MINUTE</span><span class="feature-icon"></span></div>
    <div class="wordmark">Nimbo Pebble<sup>TM</sup></div>
    <div class="contact">
      <p class="contact-title">Contact Us</p>
      <p class="contact-line">Phone, E-mail, fax Phone, E-mail, fax</p>
      <p class="contact-line">Phone, E-mail, fax</p>
    </div>
  </section>

  <p class="caption caption--front">cover front</p>
  <p class="caption caption--back">cover back</p>
</main>
</body>
</html>
```